Flyer for The Quiet Bloom Gathering

I am launching my new offering in my business at an event next Sunday where I have a booth and need a flyer advertising the offering, so the flyer needs to stand out for other practitioners that will also be there on the day offering there services.
This flyer is also what I will use for marketing on social media as well as on the day of the event. See the link below to the offering
http://sarahlindqvist.com.au/quiet-bloom-gathering/

Target Market(s)

Women with body image issues - age range 25 - 65
Women with issues around food such as binge eating, emotional eating, eating disorders.

Industry/Entity Type

Health And Wellness

Font styles to use
Serif
Sans Serif
Script

Colors
f9d9e8
85cae6
cee9f5
fee18a
ffffff
eea4c8

Requirements
Must have
• Colours matching my overall website at sarahlindqvist.com.au - pinks, light blue, gold, white
• Imagery similiar to my Instagram, see below https://www.instagram.com/riverstonecarexy/
• - soft, warm, welcoming, nurturing, safe, inviting - see image on sales page for inspiration
• contact details
Should not have
• harsh dark colours or harsh lines

```html
<!DOCTYPE html>
<html lang="en">
<head>
<meta charset="utf-8">
<title>The Quiet Bloom Gathering – Flyer</title>
<link rel="stylesheet" href="https://fonts.googleapis.com/css2?family=Great+Vibes&family=Noto+Serif:wght@400&family=Roboto:wght@300;400;500&display=swap">
<style>
  :root{
    --pink:#e8559a;
    --pink-soft:#f9d9e8;
    --pink-mid:#eea4c8;
    --blue:#85cae6;
    --blue-pale:#cee9f5;
    --navy:#1f4e8c;
    --text-blue:#2a66a3;
    --gold:#fee18a;
    --white:#ffffff;
    --ground:#ececec;
    --ink:#333;
  }
  *{box-sizing:border-box;margin:0;padding:0}
  html,body{width:1200px;height:1200px;overflow:hidden}
  body{background:var(--ground);font-family:"Roboto",sans-serif;position:relative}
  .page{position:absolute;top:240px;width:560px;height:720px;background:var(--white);overflow:hidden;box-shadow:0 4px 14px rgba(0,0,0,.12)}
  .page--front{left:26px}
  .page--back{left:614px}
  .abs{position:absolute}
  .title-small{font-family:"Noto Serif",serif;color:var(--text-blue);font-size:20px}
  .title-script{font-family:"Great Vibes",cursive;color:var(--navy);line-height:1}
  .center{text-align:center;left:0;right:0}

  /* front */
  .front-hero{left:0;top:0;width:560px;height:540px;
    background:
      radial-gradient(ellipse 120px 200px at 290px 290px,rgba(255,255,255,.95),rgba(255,255,255,0) 100%),
      radial-gradient(ellipse 230px 260px at 290px 300px,rgba(238,120,175,.75),rgba(249,217,232,0) 100%),
      linear-gradient(180deg,#7cc6ea 0%,#a9daf1 40%,#d7eef9 72%,#ffffff 96%);}
  .front-hero::after{content:"";position:absolute;inset:0;background:linear-gradient(180deg,rgba(255,255,255,0) 70%,#fff 100%)}
  .front-lead{top:413px;color:var(--pink);font-size:15px;font-weight:500;line-height:19px}
  .front-body{top:470px;color:var(--text-blue);font-size:11.5px;font-weight:300;line-height:15px}
  .front-body p+p{margin-top:10px}
  .front-ask{top:575px;color:var(--pink);font-size:19px;font-weight:300;line-height:23px}
  .brand{font-family:"Roboto",sans-serif;color:var(--pink);font-weight:300}
  .front-brand{top:635px;font-size:30px}
  .tagline{color:var(--text-blue);font-size:6.5px;font-weight:500}
  .front-tagline{top:675px}
  .front-web{top:690px;color:var(--text-blue);font-size:12px}

  /* back */
  .back-hero{left:0;top:95px;width:560px;height:320px;
    background:
      radial-gradient(ellipse 70px 90px at 115px 110px,rgba(238,120,175,.65),rgba(249,217,232,0) 100%),
      radial-gradient(ellipse 160px 170px at 360px 170px,rgba(226,196,170,.8),rgba(255,255,255,0) 100%),
      linear-gradient(180deg,#ffffff 0%,#f3f7f9 45%,#cfe0d0 78%,#b6cf8f 90%,#ffffff 100%);}
  .back-hero::after{content:"";position:absolute;inset:0;background:linear-gradient(90deg,#fff 0%,rgba(255,255,255,.6) 25%,rgba(255,255,255,0) 45%)}
  .back-call{left:20px;width:250px;top:254px;text-align:center;color:var(--ink);font-size:16px;font-weight:300;line-height:20px}
  .back-lines{top:395px;color:var(--navy);font-size:13.5px;font-weight:500;line-height:17px}
  .portrait{left:28px;top:437px;width:68px;height:68px;border-radius:50%;background:radial-gradient(circle at 50% 40%,#f5d3c2,#e49aa8 70%,#d7c3b4)}
  .back-ask{left:108px;width:440px;top:437px;text-align:center}
  .back-ask h2{color:var(--pink);font-size:19px;font-weight:400}
  .back-ask p{color:var(--ink);font-size:10px;font-weight:500;line-height:13px;margin-top:4px}
  .invite{top:508px;left:40px;right:20px;text-align:center;color:var(--ink)}
  .invite strong{display:block;font-size:14px;font-weight:500}
  .invite span{display:block;font-size:9.5px;font-weight:300;line-height:12px}
  .receive{left:42px;top:560px;width:500px;color:var(--ink)}
  .receive h3{font-size:12.5px;font-weight:500;margin-bottom:8px}
  .receive ul{list-style:none}
  .receive li{font-size:10.5px;font-weight:300;line-height:14.5px;padding-left:18px;position:relative}
  .receive li small{display:block;font-size:7px;line-height:9px}
  .receive li svg{position:absolute;left:2px;top:3px}
  .back-brand{left:48px;top:653px;font-size:26px}
  .back-tagline{left:48px;top:694px}
  .contact{left:256px;top:650px;width:296px;height:40px;background:var(--pink);color:var(--white);text-align:center;font-size:10.5px;font-weight:500;line-height:17px;padding-top:3px}
</style>
</head>
<body>

<section class="page page--front">
  <div class="abs front-hero" role="img" aria-label="Soft blue sky with clouds and a glowing pink silhouette of a woman meditating"></div>
  <div class="abs title-small" style="left:84px;top:32px">The Quiet Bloom</div>
  <div class="abs title-script" style="left:95px;top:76px;font-size:72px">Gathering</div>

  <div class="abs center front-lead">It's time to make a commitment….<br>It's time for YOU, to SHOW UP for YOU…..</div>
  <div class="abs center front-body">
    <p>It's time to truly let go……and finally heal, and find the peace that you so long for…<br>You deserve to feel the freedom that comes with truly loving and accepting your body.</p>
    <p>You deserve the freedom that comes with experiencing a deeper trusting<br>connection with your body, where you feel safe, at home.<br>Can you even imagine a whole day that you didn't hate your body,<br>you didn't fight with food, and you felt peaceful and at home with your body?</p>
  </div>
  <div class="abs center front-ask">Can you love the part of you, that hates your body?<br>You can't heal something you hate.</div>

  <div class="abs center brand front-brand">Sarah Lindqvist</div>
  <div class="abs center tagline front-tagline">Gentle Support for Peace with Your Body and Food</div>
  <div class="abs center front-web">www.sarahlindqvist.com.au</div>
</section>

<section class="page page--back">
  <div class="abs back-hero" role="img" aria-label="Woman in white sitting cross-legged on grass with arms open, beside a faint pink meditating silhouette"></div>
  <div class="abs title-small" style="left:84px;top:30px">The Quiet Bloom</div>
  <div class="abs title-script" style="left:110px;top:72px;font-size:68px">Gathering</div>

  <div class="abs back-call">It's time to show up for YOU,<br>consistently, every week,<br>and do the work,<br>once and for all.</div>

  <div class="abs center back-lines">No more games, no more half in on YOU….<br>You deserve better than a life contained in the mental prison of body hatred.</div>

  <div class="abs portrait" role="img" aria-label="Portrait of the coach seated at home"></div>
  <div class="abs back-ask">
    <h2>Are you truly ready to make the commitment?</h2>
    <p>How would it feel to be able to say, "I am free to love and accept my body",<br>and "I am free, connected and at peace to my body"?</p>
  </div>

  <div class="abs invite">
    <strong>I am inviting 10 women only into this six-week healing experience,</strong>
    <span>as I personally know, that when we share our stories, it opens our hearts for other people to share their stories. It gives us the sense we are not alone in our journey's.</span>
  </div>

  <div class="abs receive">
    <h3>The women that come on this six-week journey will receive;</h3>
    <ul>
      <li><svg width="11" height="9" viewBox="0 0 11 9"><path d="M1 4.5l3 3L10 1" fill="none" stroke="#e8559a" stroke-width="2"/></svg>One 90mins one on one coaching session with me<small>(which for the women that have attended the Friday circle previously, can be done before this healing circle begins);</small></li>
      <li><svg width="11" height="9" viewBox="0 0 11 9"><path d="M1 4.5l3 3L10 1" fill="none" stroke="#e8559a" stroke-width="2"/></svg>Private online group to continue support outside of the circle</li>
      <li><svg width="11" height="9" viewBox="0 0 11 9"><path d="M1 4.5l3 3L10 1" fill="none" stroke="#e8559a" stroke-width="2"/></svg>Homework outside of circle to support your healing</li>
      <li><svg width="11" height="9" viewBox="0 0 11 9"><path d="M1 4.5l3 3L10 1" fill="none" stroke="#e8559a" stroke-width="2"/></svg>Journal and other small gifts weekly</li>
    </ul>
  </div>

  <div class="abs brand back-brand">Sarah Lindqvist</div>
  <div class="abs tagline back-tagline">Gentle Support for Peace with Your Body and Food</div>
  <div class="abs contact">0400 555 123 &nbsp;|&nbsp; sarah@sarahlindqvist.com.au<br>www.sarahlindqvist.com.au</div>
</section>

</body>
</html>
```